A taxi bidding business needs Web Design

We need a cutting edge, super UX-intuitive, Elegant web design for our business called Fyrelo.

Fyrelo is Australia based Kind of "Next Vantro" business where user creates a trip and cabs/drivers place bids on fares/bookings/trips and lowest bidder gets the job.
User can also share the Cabs going in same route to get lowest bids.

- The design needs to be very, very intuitive to use and navigate. Please do not use much of yellow color.

References: HomQuel & Vantro

Please see the attached pdf, attaching logo as well.

Ride Sharing, Taxi

Business

5+ page

Must have
• Icons/graphics, How it works icons, case studies icons, all mentioned pages
Should not have
• Not much yellow color

```html
<!DOCTYPE html>
<html lang="en">
<head>
<meta charset="utf-8">
<title>Fyrelo — Low Bids, Lowest Fares</title>
<link href="https://fonts.googleapis.com/css2?family=Roboto:wght@300;400;500;700;900&display=swap" rel="stylesheet">
<style>
:root{
  --navy:#14265c;
  --navy-deep:#0f1d48;
  --navy-text:#1b2b5e;
  --yellow:#f7c31d;
  --ink:#222;
  --muted:#777b86;
  --line:#e3e5ea;
  --white:#fff;
  --footer:#1f1f1f;
  --footer-text:#c9c9c9;
}
*{margin:0;padding:0;box-sizing:border-box}
html,body{width:1200px;height:4712px;overflow:hidden}
body{font-family:"Roboto",sans-serif;color:var(--ink);background:var(--white);position:relative}
.abs{position:absolute}
.section{position:absolute;left:0;width:1200px}
.lorem{font-size:12px;line-height:17px;color:var(--muted)}

/* header */
.topbar{top:0;left:620px;width:580px;height:24px;background:var(--navy);color:#fff;font-size:10px;display:flex;align-items:center;gap:26px;padding-left:22px}
.topbar span b{font-weight:700}
.header{top:0;height:95px}
.brand{display:flex;align-items:center;gap:8px;font-weight:900;letter-spacing:1px}
.brand .dot{width:16px;height:16px;border-radius:50%;background:#e0312b}
.header .brand{position:absolute;left:250px;top:40px;font-size:20px;color:var(--navy-text)}
.nav{position:absolute;right:245px;top:52px;display:flex;gap:14px;font-size:10px;font-weight:500;color:#333}

/* hero */
.hero{top:95px;height:570px;background:linear-gradient(100deg,#3b3f45 0%,#6c7078 45%,#b9b5ae 75%,#d9d2c6 100%)}
.hero-shade{inset:0;background:linear-gradient(90deg,rgba(15,18,30,.55),rgba(15,18,30,0) 60%)}
.hero-title{position:absolute;left:250px;top:180px;color:var(--yellow);font-size:40px;line-height:46px;font-weight:900}
.hero-title .cap{font-variant:small-caps}
.hero-lead{position:absolute;left:250px;top:340px;width:380px;color:#fff;font-size:13px;line-height:18px}
.btn-yellow{background:var(--yellow);color:#222;font-size:11px;font-weight:700;border-radius:16px;display:inline-block;text-align:center}
.hero-cta{position:absolute;left:250px;top:392px;width:86px;height:28px;line-height:28px}
.signin{position:absolute;left:707px;top:119px;width:245px;height:361px;background:#fff;padding:28px 22px}
.signin-title{color:var(--yellow);font-size:26px;font-weight:900;font-variant:small-caps}
.signin-note{font-size:10px;line-height:14px;margin-top:8px;color:var(--muted)}
.field{border-bottom:1px solid var(--line);font-size:10px;color:#999;height:30px;line-height:36px;margin-top:26px}
.signin-submit{margin-top:28px;width:98px;height:28px;line-height:28px}

/* services */
.services{top:665px;height:545px;background:var(--navy);color:#fff}
.h-section{font-size:36px;font-weight:900;text-align:center}
.services .h-section{margin-top:58px}
.services .intro{width:580px;margin:18px auto 0;color:#d6dbea;font-size:12px;line-height:17px;text-align:center}
.svc{position:absolute;top:208px;width:226px}
.svc .photo{height:127px}
.svc h3{font-size:16px;font-weight:900;margin-top:26px}
.svc p{font-size:11px;line-height:15px;color:#d6dbea;margin-top:8px}
.svc .more{font-size:11px;font-weight:700;margin-top:12px;display:block;text-decoration:underline}

/* how it works */
.how{top:1210px;height:595px}
.how .h-section{margin-top:66px;color:var(--navy-text)}
.how .intro{width:560px;margin:18px auto 0;text-align:center}
.step{position:absolute;width:232px}
.step svg{width:32px;height:32px}
.step h4{font-size:11px;font-weight:900;color:var(--navy-text);margin-top:10px;white-space:nowrap}
.step p{font-size:11px;line-height:15px;color:var(--muted);margin-top:4px;width:200px}

/* about */
.about{top:1805px;height:505px}
.about h2{position:absolute;left:250px;top:36px;font-size:40px;font-weight:900;color:var(--navy-text)}
.about .copy{position:absolute;left:250px;top:118px;width:330px}
.about .copy p+p{margin-top:16px}
.btn-navy{position:absolute;background:var(--navy);color:#fff;font-size:11px;font-weight:700;border-radius:16px;text-align:center}
.about .btn-navy{left:250px;top:378px;width:104px;height:28px;line-height:28px}
.about .photo{position:absolute;left:628px;top:29px;width:572px;height:374px;background:linear-gradient(120deg,#c9cdd3,#8c96a6 50%,#dfe3e8)}

/* drive */
.drive{top:2310px;height:345px}
.drive .photo{position:absolute;left:0;top:0;width:568px;height:335px;background:linear-gradient(160deg,#f1d48a,#c9a15a 45%,#7b6a4c)}
.drive h2{position:absolute;left:590px;top:12px;font-size:32px;font-weight:900;color:var(--navy-text)}
.drive h5{position:absolute;left:590px;top:52px;font-size:15px;font-weight:700;color:var(--navy-text)}
.drive .intro{position:absolute;left:590px;top:80px;width:360px;font-size:11px;line-height:15px}
.feat{position:absolute;width:210px;display:flex;gap:10px}
.feat svg{width:24px;height:24px;flex:none}
.feat h4{font-size:13px;font-weight:900;color:var(--navy-text)}
.feat p{font-size:10px;line-height:14px;color:var(--muted);margin-top:3px}

/* testimonials */
.clients{top:2725px;height:557px;background:var(--navy);color:#fff;text-align:center}
.clients .h-section{margin-top:66px}
.clients .intro{width:580px;margin:20px auto 0;color:#d6dbea;font-size:12px;line-height:17px}
.avatar{width:84px;height:84px;border-radius:50%;margin:34px auto 0;background:linear-gradient(160deg,#9aa4b8,#4e5a76);border:3px solid #fff}
.clients h4{font-size:15px;font-weight:700;margin-top:10px}
.clients .role{font-size:10px;color:#d6dbea}
.clients .quote{width:700px;margin:16px auto 0;font-size:11px;line-height:16px;color:#e7eaf3}
.clients .marks{font-size:54px;font-weight:900;line-height:40px;margin-top:24px}
.dots{display:flex;gap:6px;justify-content:center;margin-top:10px}
.dots i{width:8px;height:8px;border-radius:50%;background:#6d7aa3}
.dots i:first-child{background:#fff}

/* map */
.map{top:3290px;height:362px;background:linear-gradient(135deg,#e6e1d3,#d8dfc8 40%,#c9dbe8 70%,#e9e4d6)}
.estimate{position:absolute;left:597px;top:101px;width:351px;height:164px;background:rgba(20,38,92,.9);padding:24px 24px}
.estimate h3{color:#fff;font-size:18px;font-weight:700}
.estimate .input{background:#fff;height:32px;margin-top:14px;font-size:10px;color:#555;display:flex;align-items:center;justify-content:space-between;padding:0 12px}
.estimate h3+.input{margin-top:20px}

/* sign in band */
.band{top:3652px;height:163px;background:var(--navy);color:#fff}
.band h3{position:absolute;left:250px;top:55px;font-size:24px;line-height:28px;font-weight:900}
.band .btn-white{position:absolute;left:747px;top:68px;width:183px;height:36px;line-height:36px;background:#fff;color:var(--navy-text);border-radius:18px;font-size:12px;font-weight:700;text-align:center}

/* help cards */
.help{top:3815px;height:315px}
.card{position:absolute;top:74px;width:200px}
.card .ico{width:70px;height:70px;border-radius:50%}
.card h4{font-size:14px;font-weight:900;color:var(--navy-text);margin-top:20px}
.card ul{list-style:none;margin-top:8px;font-size:11px;line-height:16px;color:#555}
.card .more{font-size:11px;font-weight:700;color:var(--navy-text);margin-top:4px}

/* footer */
.footer{top:4130px;height:582px;background:var(--footer);color:var(--footer-text)}
.footer .brand{position:absolute;left:250px;top:62px;font-size:22px;color:#fff}
.pill-out{position:absolute;top:78px;height:30px;line-height:30px;background:#fff;color:#222;border-radius:15px;font-size:10px;font-weight:700;text-align:center}
.fcol{position:absolute;top:197px;list-style:none;font-size:10px;line-height:18px}
.fcol .head{color:#fff;font-weight:700}
.store{position:absolute;left:250px;width:112px;height:30px;border-radius:6px;background:#000;border:1px solid #777}
.footer .rule{position:absolute;left:250px;top:500px;width:700px;height:1px;background:#3a3a3a}
.copy-note{position:absolute;left:250px;top:520px;font-size:10px}
.legal{position:absolute;left:800px;top:520px;font-size:10px}
.social{position:absolute;top:496px;width:58px;height:58px;border-radius:50%;border:3px solid #fff}
</style>
</head>
<body>

<header class="section header">
  <div class="brand"><span class="dot"></span>FYRELO</div>
  <nav class="nav"><span>HOME</span><span>DRIVER SIGN UP</span><span>USER SIGN UP</span><span>SIGN IN</span><span>DRIVE</span><span>CITIES</span><span>HELP</span></nav>
</header>
<div class="abs topbar"><span>Ride &nbsp;|&nbsp; Drive &nbsp;|&nbsp; Help &nbsp;|&nbsp; Sign In</span><span>Phone Number : <b>1300 555 014</b></span></div>

<section class="section hero" role="img" aria-label="Smiling woman sitting in a car">
  <div class="abs hero-shade"></div>
  <h1 class="hero-title"><span class="cap">Welcome To</span><br>Roam Around Low<br>Bids, Lowest Fares</h1>
  <p class="hero-lead">Book a trip in seconds and let nearby drivers compete with their best bid.</p>
  <span class="btn-yellow hero-cta">Read More</span>
  <form class="signin">
    <h2 class="signin-title">Sign In</h2>
    <p class="signin-note">Sign in to post a trip, compare driver bids and track your bookings.</p>
    <div class="field">Name</div>
    <div class="field">Email</div>
    <div class="field">Password</div>
    <span class="btn-yellow signin-submit">Submit Now</span>
  </form>
</section>

<section class="section services">
  <h2 class="h-section">Services</h2>
  <p class="intro">Post your trip once and drivers across the city send their offers. Compare fares, ratings and arrival times, then pick the ride that suits you best every time.</p>
  <div class="svc" style="left:248px">
    <div class="photo" role="img" aria-label="Passengers riding in a cab" style="background:linear-gradient(135deg,#c9a27a,#7c5a3e)"></div>
    <h3>CABS/DRIVERS</h3>
    <p>Verified local drivers with rated profiles, clean cars and fair prices, ready to bid on your next trip across town.</p>
    <span class="more">Read More</span>
  </div>
  <div class="svc" style="left:487px">
    <div class="photo" role="img" aria-label="Hands counting cash fares" style="background:linear-gradient(135deg,#d8c6a0,#8f7a55)"></div>
    <h3>BIDS ON FARES</h3>
    <p>Drivers place live bids on every trip you post, so the fare keeps dropping until you choose the lowest offer.</p>
    <span class="more">Read More</span>
  </div>
  <div class="svc" style="left:726px">
    <div class="photo" role="img" aria-label="Couple planning a booked trip" style="background:linear-gradient(135deg,#a9b8c9,#5d6c80)"></div>
    <h3>BOOKINGS/TRIPS</h3>
    <p>Schedule trips ahead, share a cab going the same way and keep every booking and receipt in a single place.</p>
    <span class="more">Read More</span>
  </div>
</section>

<section class="section how">
  <h2 class="h-section">How it works</h2>
  <p class="intro lorem">Create a trip, receive bids from nearby drivers and accept the best one. Share the route with other riders to bring your fare down even further.</p>

  <div class="step" style="left:248px;top:286px">
    <svg viewBox="0 0 32 32" fill="none" stroke="#222" stroke-width="3"><circle cx="16" cy="16" r="12"/><path d="M7 7l18 18"/></svg>
    <h4>INSTANT BIDS, SLASHED FARES</h4><p>Bids arrive within moments of posting, pushing prices lower.</p>
  </div>
  <div class="step" style="left:500px;top:286px">
    <svg viewBox="0 0 32 32" fill="none" stroke="#222" stroke-width="3"><path d="M5 22a11 11 0 1 1 22 0"/><path d="M16 22l6-8"/></svg>
    <h4>AUTOMATED BIDDING, SAVES TIME</h4><p>Set your price limit once and let the system match drivers.</p>
  </div>
  <div class="step" style="left:748px;top:286px">
    <svg viewBox="0 0 32 32" fill="#222"><path d="M13 2h6l1 4 4 2 4-2 3 5-3 3v4l3 3-3 5-4-2-4 2-1 4h-6l-1-4-4-2-4 2-3-5 3-3v-4l-3-3 3-5 4 2 4-2z"/><circle cx="16" cy="16" r="5" fill="#fff"/></svg>
    <h4>SPEEDY SERVICE ANYWHERE ANYTIME</h4><p>Drivers are on the road day and night in every major city.</p>
  </div>
  <div class="step" style="left:248px;top:438px">
    <svg viewBox="0 0 32 32" fill="none" stroke="#222" stroke-width="2.5"><circle cx="11" cy="11" r="5"/><circle cx="22" cy="13" r="4"/><path d="M2 28c0-6 4-9 9-9s9 3 9 9M20 20c5 0 9 2 9 8"/></svg>
    <h4>MULTIPLE HIRING, HUGE DISCOUNTS</h4><p>Book several cabs for a group and unlock lower rates.</p>
  </div>
  <div class="step" style="left:500px;top:438px">
    <svg viewBox="0 0 32 32" fill="#222"><path d="M8 5h16l6 8-14 15L2 13z"/></svg>
    <h4>LUXURY HIRES</h4><p>Premium sedans and SUVs for events, airports and business.</p>
  </div>
  <div class="step" style="left:748px;top:438px">
    <svg viewBox="0 0 32 32" fill="#222"><path d="M2 7h10l3 3h15v17H2z"/></svg>
    <h4>SAVE SMART</h4><p>Track spending and see how much every trip has saved you.</p>
  </div>
</section>

<section class="section about">
  <h2>About us</h2>
  <div class="copy lorem">
    <p>Fyrelo began in Australia with a simple idea: riders should set the pace on price. Instead of fixed fares, drivers compete for each trip, and the lowest fair bid wins. Riders save money, drivers fill empty hours, and cities get fewer empty cabs circling the streets.</p>
    <p>Today we connect thousands of riders with trusted local drivers. Every driver is checked and rated, every fare is shown upfront, and shared routes let people travelling the same way split the cost. We keep improving the app so booking a ride feels quick, clear and fair for everyone involved.</p>
  </div>
  <span class="btn-navy">Read More</span>
  <div class="photo" role="img" aria-label="Smiling driver in a car giving a thumbs up"></div>
</section>

<section class="section drive">
  <div class="photo" role="img" aria-label="Friends raising hands in an open car on a sunny road"></div>
  <h2>Drive</h2>
  <h5>How Fyrelo work ?</h5>
  <p class="intro lorem">Sign up as a driver, go online in your area and start bidding on trips that fit your route and your schedule.</p>
  <div class="feat" style="left:590px;top:166px">
    <svg viewBox="0 0 24 24" fill="none" stroke="#222" stroke-width="2"><path d="M2 4h3l3 11h12l2-8H7"/><circle cx="9" cy="19" r="1.6"/><circle cx="18" cy="19" r="1.6"/></svg>
    <div><h4>Go Online</h4><p>Open the app and see trips posted near you.</p></div>
  </div>
  <div class="feat" style="left:816px;top:166px">
    <svg viewBox="0 0 24 24" fill="#222"><circle cx="12" cy="7" r="5"/><path d="M3 23c0-6 4-9 9-9s9 3 9 9z"/></svg>
    <div><h4>Accept Incoming Job</h4><p>Confirm the rider once your bid is chosen.</p></div>
  </div>
  <div class="feat" style="left:590px;top:270px">
    <svg viewBox="0 0 24 24" fill="#222"><path d="M13 2l8 8-3 3-8-8z"/><path d="M11 8l4 4-10 10-4-4z"/></svg>
    <div><h4>Bid And Win</h4><p>Offer your best fare and win the booking.</p></div>
  </div>
  <div class="feat" style="left:816px;top:270px">
    <svg viewBox="0 0 24 24" fill="#222"><circle cx="12" cy="6" r="4"/><path d="M4 22c0-7 4-10 8-10s8 3 8 10z"/></svg>
    <div><h4>Drive</h4><p>Pick up your rider and get paid after each trip.</p></div>
  </div>
</section>

<section class="section clients">
  <h2 class="h-section">What Clients say</h2>
  <p class="intro">Riders and drivers share how bidding on fares has changed the way they travel and work around their cities.</p>
  <div class="avatar" role="img" aria-label="Client portrait"></div>
  <h4>Jordan Reeve</h4>
  <div class="role">Regular rider</div>
  <p class="quote">I post my airport trip the night before and wake up to three or four bids already waiting. The fares are far lower than a regular cab, the drivers are friendly, and sharing the ride with a neighbour on the same route cut my cost almost in half again.</p>
  <div class="marks">&rdquo;</div>
  <div class="dots"><i></i><i></i><i></i><i></i></div>
</section>

<section class="section map" role="img" aria-label="City street map">
  <form class="estimate">
    <h3>PRICING GET A FARE ESTIMATE</h3>
    <div class="input">Enter pickup location
      <svg width="12" height="12" viewBox="0 0 12 12"><path d="M11 1L1 5l5 1 1 5z" fill="#333"/></svg></div>
    <div class="input">Enter destination
      <svg width="12" height="12" viewBox="0 0 12 12"><path d="M1 6h9M7 3l3 3-3 3" stroke="#333" stroke-width="1.5" fill="none"/></svg></div>
  </form>
</section>

<section class="section band">
  <h3>SIGN IN TO GET HELP WITH YOUR<br>ACCOUNT AND TRIPS</h3>
  <span class="btn-white">SIGN IN</span>
</section>

<section class="section help">
  <div class="card" style="left:250px">
    <div class="ico" style="background:var(--navy)"></div>
    <h4>A GUIDE TO FYRELO</h4>
    <ul><li>How to post a trip</li><li>How bids work</li><li>Sharing a ride</li></ul>
    <div class="more">More</div>
  </div>
  <div class="card" style="left:505px">
    <div class="ico" style="background:#ef8a2a"></div>
    <h4>DRIVING WITH FYRELO</h4>
    <ul><li>Sign up to drive</li><li>Placing your first bid</li><li>Getting paid</li></ul>
    <div class="more">More</div>
  </div>
  <div class="card" style="left:772px">
    <div class="ico" style="background:#e2432f"></div>
    <h4>ACCOUNT AND PAYMENT</h4>
    <ul><li>I can't sign in to my account</li><li>Account settings and ratings</li><li>Receipts and refunds</li></ul>
    <div class="more">More</div>
  </div>
</section>

<footer class="section footer">
  <div class="brand"><span class="dot"></span>FYRELO</div>
  <span class="pill-out" style="left:537px;width:143px">SIGN UP TO RIDE</span>
  <span class="pill-out" style="left:808px;width:143px">SIGN UP TO DRIVE</span>

  <ul class="fcol" style="left:250px"><li>Enter Your Location</li><li>ENGLISH</li><li>Help/Help</li></ul>
  <div class="store" style="top:290px"></div>
  <div class="store" style="top:328px"></div>
  <ul class="fcol" style="left:388px"><li>Ride</li><li>Drive</li><li>Cities</li><li>Fare Estimator</li><li>Deliver</li><li>Food</li><li>Business Travel</li><li>How it Works</li><li>Airports</li></ul>
  <ul class="fcol" style="left:537px"><li>Safety</li><li>Careers</li><li>Helping Other</li><li>Our Story</li><li>Newsroom</li><li>Media</li><li>Fyrelo API</li><li>Gift Cards</li><li>Fyrelo vs Driving Jobs</li></ul>
  <ul class="fcol" style="left:682px"><li class="head">TOP CITIES</li><li>USA</li><li>France</li><li>India</li><li>Spain</li><li>Mexico</li></ul>
  <ul class="fcol" style="left:827px"><li class="head">TOP CITIES</li><li>Australia</li><li>San Francisco</li><li>London</li><li>Los Angeles</li><li>Washington D.C.</li><li>Mexico City</li><li>Sao Paulo</li><li>Dubai</li></ul>

  <div class="rule"></div>
  <div class="copy-note">&copy; 2017 Fyrelo. All rights reserved.</div>
  <div class="legal">Privacy &nbsp;|&nbsp; Advertise &nbsp;|&nbsp; Terms</div>
  <div class="social" style="left:486px;background:#3b5693"></div>
  <div class="social" style="left:574px;background:#2a76b5"></div>
  <div class="social" style="left:662px;background:#41a6e0"></div>
</footer>

</body>
</html>
```